Women's Health Company needs business card

We need a business card for a USA based women's health care company. We use digital technology to enhance therapy prescribed by clinicians for their patients

```html
<!DOCTYPE html>
<html lang="en">
<head>
<meta charset="utf-8">
<title>Veloria Health – Business Card</title>
<link href="https://fonts.googleapis.com/css2?family=Raleway:wght@400;500;700&display=swap" rel="stylesheet">
<style>
  :root {
    --bg: #e9eaec;
    --card: #ffffff;
    --teal: #5dbab3;
    --purple: #8d4fa8;
    --ink: #4a4a4a;
    --shadow: rgba(0,0,0,0.12);
  }
  * { margin: 0; padding: 0; box-sizing: border-box; }
  html, body { width: 1200px; height: 900px; overflow: hidden; background: var(--bg); }
  .canvas {
    width: 1200px; height: 900px;
    display: flex; align-items: center; justify-content: center; gap: 60px;
  }
  .card {
    position: relative;
    width: 520px; height: 297px;
    background: var(--card);
    box-shadow: 0 6px 20px var(--shadow);
  }
  .brand {
    display: flex; align-items: center; gap: 8px;
    font-family: 'Raleway', sans-serif; font-weight: 500;
    color: var(--teal); letter-spacing: 0.5px;
  }
  .brand-dot { width: 10px; height: 10px; border-radius: 50%; background: var(--purple); }

  /* contact side */
  .card-contact .brand { position: absolute; left: 34px; top: 34px; font-size: 30px; }
  .divider {
    position: absolute; left: 34px; right: 34px; top: 168px;
    height: 1.5px; background: var(--teal);
  }
  .person { position: absolute; right: 34px; top: 112px; text-align: right; font-family: 'Raleway', sans-serif; }
  .person-name { font-size: 26px; font-weight: 700; color: var(--purple); line-height: 1.1; }
  .person-role { font-size: 14px; color: var(--ink); margin-top: 2px; }
  .address {
    position: absolute; left: 34px; top: 184px;
    font-family: Arial, Helvetica, sans-serif; font-size: 12px; color: var(--ink); line-height: 1.45;
  }
  .contacts {
    position: absolute; right: 34px; top: 184px;
    list-style: none; font-family: Arial, Helvetica, sans-serif; font-size: 13px; color: var(--ink);
  }
  .contacts li { display: flex; justify-content: flex-end; align-items: center; gap: 7px; line-height: 22px; }
  .contacts svg { width: 13px; height: 13px; fill: var(--purple); }

  /* logo side */
  .card-front { display: flex; align-items: center; justify-content: center; }
  .card-front .brand { font-size: 40px; }
  .card-front .brand-dot { width: 14px; height: 14px; }
</style>
</head>
<body>
<main class="canvas">
  <section class="card card-contact">
    <div class="brand"><span class="brand-dot"></span>Veloria Health</div>
    <div class="person">
      <div class="person-name">Daniel Porter</div>
      <div class="person-role">President and CEO</div>
    </div>
    <div class="divider"></div>
    <address class="address" style="font-style:normal">48 Harbour Lane, Kingston<br>ON Canada K7L 2R4</address>
    <ul class="contacts">
      <li>(+1) 555 014 2297
        <svg viewBox="0 0 24 24"><path d="M6.6 10.8a15.1 15.1 0 0 0 6.6 6.6l2.2-2.2a1 1 0 0 1 1-.25 11.4 11.4 0 0 0 3.6.57 1 1 0 0 1 1 1V20a1 1 0 0 1-1 1A17 17 0 0 1 3 4a1 1 0 0 1 1-1h3.5a1 1 0 0 1 1 1c0 1.25.2 2.45.57 3.6a1 1 0 0 1-.25 1z"/></svg>
      </li>
      <li>info@veloriahealth.com
        <svg viewBox="0 0 24 24"><path d="M2 5h20v14H2z M4 7v.5l8 5 8-5V7z" fill-rule="evenodd"/></svg>
      </li>
      <li>www.veloriahealth.com
        <svg viewBox="0 0 24 24"><circle cx="12" cy="12" r="10"/><path d="M2 12h20M12 2c3 3 3 17 0 20M12 2c-3 3-3 17 0 20" stroke="#fff" stroke-width="1.3" fill="none"/></svg>
      </li>
    </ul>
  </section>

  <section class="card card-front">
    <div class="brand"><span class="brand-dot"></span>Veloria Health</div>
  </section>
</main>
</body>
</html>
```